Business Card Design

We are a General Practice - Family medicine
We also have Allied Health professionals working within our team

Industry/Entity Type

Business

Contact Information for Business Card

Front of the card to display:

BRAMBLEWICK MEDICAL
PHONE 6348 2917

5/41 Fennimore Parade
Launceston Tasmania 7284

Back of the card to display:

My Appointments
Date:
Time:
With:

Please remember to phone us on 6348 2917 to cancel your appointment if you can't keep it.
A fee applied to missed appointments

```html
<!DOCTYPE html>
<html lang="en">
<head>
<meta charset="utf-8">
<title>Bramblewick Medical – Business Cards</title>
<link rel="stylesheet" href="https://fonts.googleapis.com/css2?family=Ubuntu:wght@400&family=Open+Sans:wght@400;700&display=swap">
<style>
  :root {
    --backdrop: #9b9b9b;
    --card: #ffffff;
    --brand-blue: #1f9fd3;
    --brand-blue-deep: #1787b8;
    --name-blue: #2b86bf;
    --leaf-green: #8cc63f;
    --label-grey: #8a8f93;
    --shadow: rgba(0, 0, 0, 0.28);
  }
  * { box-sizing: border-box; margin: 0; padding: 0; }
  html, body {
    width: 1200px; height: 900px; overflow: hidden;
    background: var(--backdrop);
    font-family: "Open Sans", Arial, sans-serif;
  }
  .stage {
    position: relative; width: 1200px; height: 900px;
    display: flex; justify-content: center; align-items: center; gap: 60px;
  }
  .card {
    position: relative; width: 330px; height: 560px;
    background: var(--card); border-radius: 6px;
    box-shadow: 0 14px 30px var(--shadow);
    overflow: hidden;
  }
  .brand {
    position: absolute; left: 0; right: 0; text-align: center;
  }
  .brand__dot {
    display: block; margin: 0 auto 14px;
    width: 54px; height: 54px; border-radius: 50%;
    background: var(--leaf-green);
  }
  .brand__name {
    font-family: "Ubuntu", "Open Sans", sans-serif; font-weight: 400;
    font-size: 33px; line-height: 1; color: var(--name-blue);
    letter-spacing: -0.3px;
  }
  .brand__tagline {
    margin-top: 8px; font-size: 10.5px; letter-spacing: 4px;
    color: var(--label-grey); text-transform: uppercase;
  }

  /* Front */
  .card--front .brand { top: 56px; }
  .info-panel {
    position: absolute; left: 18px; right: 18px;
    background: var(--brand-blue); border-radius: 12px;
    color: #fff; text-align: center; font-weight: 700;
  }
  .info-panel--phone { top: 220px; height: 150px; padding-top: 74px; }
  .info-panel--address { top: 408px; height: 122px; padding-top: 62px; }
  .info-panel__icon {
    position: absolute; left: 50%; transform: translateX(-50%);
    width: 56px; height: 56px;
  }
  .info-panel--phone .info-panel__icon { top: 10px; }
  .info-panel--address .info-panel__icon { top: -28px; }
  .info-panel__label { font-size: 19px; letter-spacing: 0.3px; line-height: 1.1; }
  .info-panel__phone { font-size: 28px; line-height: 1.25; }
  .info-panel__address { font-size: 17.5px; line-height: 1.3; }

  /* Back */
  .card--back .brand { top: 40px; }
  .ribbon {
    position: absolute; left: 22px; top: 170px; width: 286px; height: 52px;
    transform: rotate(-7deg);
  }
  .ribbon__text {
    position: absolute; inset: 0; display: flex; align-items: center; justify-content: center;
    color: #fff; font-size: 21px; letter-spacing: 1.5px; font-weight: 400;
  }
  .appt-fields { position: absolute; left: 26px; right: 26px; top: 262px; }
  .appt-field {
    display: flex; align-items: flex-end; height: 44px;
    color: var(--label-grey); font-size: 17px;
  }
  .appt-field__line {
    flex: 1; margin-left: 8px; margin-bottom: 5px;
    border-bottom: 2px dotted var(--brand-blue);
  }
  .appt-note {
    position: absolute; left: 18px; right: 18px; top: 410px;
    text-align: center; color: var(--brand-blue); font-weight: 700;
    font-size: 13.5px; line-height: 1.45;
  }
  .appt-note__phone { display: block; font-size: 20px; line-height: 1.25; }
</style>
</head>
<body>
<main class="stage">

  <section class="card card--back" aria-label="Appointment card, back">
    <div class="brand">
      <span class="brand__dot"></span>
      <div class="brand__name">Bramblewick Medical</div>
      <div class="brand__tagline">Healthcare Centre</div>
    </div>

    <div class="ribbon">
      <svg width="286" height="52" viewBox="0 0 286 52" aria-hidden="true">
        <polygon points="0,10 30,10 30,46 0,46 12,28" fill="var(--brand-blue-deep)"/>
        <polygon points="286,10 256,10 256,46 286,46 274,28" fill="var(--brand-blue-deep)"/>
        <rect x="18" y="4" width="250" height="40" fill="var(--brand-blue)"/>
      </svg>
      <span class="ribbon__text">APOINTMENT</span>
    </div>

    <div class="appt-fields">
      <div class="appt-field"><span>Date</span><span class="appt-field__line"></span></div>
      <div class="appt-field"><span>Time</span><span class="appt-field__line"></span></div>
      <div class="appt-field"><span>With</span><span class="appt-field__line"></span></div>
    </div>

    <p class="appt-note">
      Please remember to phone us on
      <span class="appt-note__phone">6348 2917</span>
      to cancel your appointment if you can't keep it.<br>
      A fee applied to missed appointments
    </p>
  </section>

  <section class="card card--front" aria-label="Business card, front">
    <div class="brand">
      <span class="brand__dot"></span>
      <div class="brand__name">Bramblewick Medical</div>
    </div>

    <div class="info-panel info-panel--phone">
      <svg class="info-panel__icon" viewBox="0 0 56 56" aria-hidden="true">
        <circle cx="28" cy="28" r="25" fill="none" stroke="#fff" stroke-width="3"/>
        <path d="M20 16c2-1 3 0 4 2l2 4c1 2 0 3-1 4l-1 1c1 3 4 6 7 7l1-1c1-1 2-2 4-1l4 2c2 1 3 2 2 4-1 3-4 4-7 3-8-2-14-8-16-16-1-3 0-8 1-9z" fill="#fff"/>
      </svg>
      <div class="info-panel__label">HEALTCARE CENTRE</div>
      <div class="info-panel__phone">6348 2917</div>
    </div>

    <div class="info-panel info-panel--address">
      <svg class="info-panel__icon" viewBox="0 0 56 56" aria-hidden="true">
        <circle cx="28" cy="28" r="26" fill="var(--brand-blue)" stroke="#fff" stroke-width="3"/>
        <path d="M14 38l8-4 12 4 8-4v-14l-8 4-12-4-8 4z" fill="none" stroke="#fff" stroke-width="2.2" stroke-linejoin="round"/>
        <path d="M28 32c-5-6-7-9-7-12a7 7 0 0 1 14 0c0 3-2 6-7 12z" fill="#fff"/>
        <circle cx="28" cy="20" r="2.6" fill="var(--brand-blue)"/>
      </svg>
      <div class="info-panel__address">5/41 Fennimore Parade<br>Launceston Tasmania 7284</div>
    </div>
  </section>

</main>
</body>
</html>
```